Brovik Pty Ltd business card design

We need a business card for our company who is involved in upper market residential property development.
Design should be elegant and contemporary.

Our residences are inspired and elegant in contemporary design, combined with inviting ambience. We produce exclusive boutique developments which appeal to the most discerning of purchasers.
We would like to see a design to reflect the above.
Updates

Industry/Entity Type

Residential

Contact Information for Business Card

Brovik Pty Ltd, Marco Sidlewski, PO Box 58 Larkdale 3190 Melbourne AUSTRALIA, ph (+61 3) 0427 5096 82

Logo Text

Brovik Pty Ltd

```html
<!DOCTYPE html>
<html lang="en">
<head>
<meta charset="utf-8">
<title>Brovik Pty Ltd – Business Card</title>
<link rel="stylesheet" href="https://fonts.googleapis.com/css2?family=Montserrat:wght@400;500;600;700&display=swap">
<style>
  :root {
    --card-bg: #c9c8c6;
    --ink: #2a2a2a;
    --ink-soft: #333333;
  }
  html, body {
    margin: 0;
    padding: 0;
    width: 1200px;
    height: 741px;
    overflow: hidden;
    background: var(--card-bg);
  }
  .card {
    position: relative;
    width: 1200px;
    height: 741px;
    background: var(--card-bg);
    color: var(--ink);
    font-family: "Montserrat", sans-serif;
    text-align: center;
  }
  .card > * {
    position: absolute;
    left: 0;
    right: 0;
    margin: 0;
    line-height: 1;
  }
  .brand-mark {
    top: 178px;
    font-size: 54px;
    font-weight: 500;
    letter-spacing: 1px;
    color: var(--ink);
  }
  .person-name {
    top: 350px;
    font-size: 36px;
    font-weight: 700;
    letter-spacing: 0.3px;
  }
  .person-credentials {
    top: 388px;
    font-size: 21px;
    font-weight: 400;
    letter-spacing: 1px;
    color: var(--ink-soft);
  }
  .contact-phone {
    top: 427px;
    font-size: 27px;
    font-weight: 400;
    letter-spacing: 1px;
  }
  .contact-email {
    top: 459px;
    font-size: 25px;
    font-weight: 400;
  }
  .company-name {
    top: 528px;
    font-size: 31px;
    font-weight: 500;
  }
  .company-division {
    top: 559px;
    font-size: 21px;
    font-weight: 400;
    color: var(--ink-soft);
  }
  .company-address {
    top: 589px;
    font-size: 22px;
    font-weight: 400;
    letter-spacing: -0.2px;
    color: var(--ink-soft);
  }
</style>
</head>
<body>
  <main class="card">
    <p class="brand-mark">Brovik Pty Ltd</p>
    <h1 class="person-name">MARCO SIDLEWSKI</h1>
    <p class="person-credentials">B.SC, ND</p>
    <p class="contact-phone">(+61 3) 0427 5096 82</p>
    <p class="contact-email">marco.sidlewski@kestrelmail.com</p>
    <p class="company-name">BROVIK PTY LTD</p>
    <p class="company-division">PROPERTY GROUP</p>
    <p class="company-address">PO Box 58 Larkdale 3190 Melbourne AUSTRALIA</p>
  </main>
</body>
</html>
```